Deck Construction Company Billboard Design needed

We are a deck company with a 10'x32' billboard to fill with an advertisement. I'd like this ad to be 75% photo, 25% color-filled background with white text over (space to be divided side-to-side with line of some sort). This billboard artwork must be clearly legible and simple. The information I need on the billboard is as follows:
Plank QR (company name)
plankqr.ca
Outdoor Living Spaces
416-283-9061
Attached is a copy of the logo and photos I'd like to use (please choose one photo per billboard design)

Target Market(s)

30-70 year old home owners

Industry/Entity Type

Deck Builder

Font styles to use
Other font styles liked:
• Calibri

Colors
0054AA
0677BA
7BADD7
CADEEF
E8F1F8

Requirements
Must have
• Clear, simple white text. Dark blue fill, red accent
Nice to have
• Layering of photo and text
Should not have
• Too much to read

```html
<!DOCTYPE html>
<html lang="en">
<head>
<meta charset="utf-8">
<title>Plank QR – Outdoor Living Spaces Billboard</title>
<link href="https://fonts.googleapis.com/css2?family=Montserrat:wght@700;800&display=swap" rel="stylesheet">
<style>
  :root {
    --navy: #0e2a4b;
    --red: #e10600;
    --white: #ffffff;
    --ink: #262626;
    --page: #eef1f4;
    --photo-fill: #a3aba3;
  }
  * { margin: 0; padding: 0; box-sizing: border-box; }
  html, body {
    width: 1200px;
    height: 1200px;
    overflow: hidden;
    background: var(--page);
    font-family: "Montserrat", sans-serif;
  }
  .billboard {
    position: absolute;
    left: 0;
    top: 412px;
    width: 1200px;
    height: 375px;
    background: var(--white);
    overflow: hidden;
  }
  .billboard-shapes {
    position: absolute;
    inset: 0;
    width: 1200px;
    height: 375px;
  }
  .brand-name {
    position: absolute;
    top: 28px;
    left: 760px;
    width: 380px;
    text-align: center;
    font-weight: 800;
    font-size: 54px;
    letter-spacing: 1px;
    color: var(--ink);
    line-height: 1;
    white-space: nowrap;
  }
  .headline {
    position: absolute;
    top: 124px;
    left: 690px;
    width: 500px;
    text-align: center;
    font-weight: 800;
    font-size: 48px;
    line-height: 1.12;
    color: var(--white);
    letter-spacing: 1px;
    white-space: nowrap;
  }
  .contact-row {
    position: absolute;
    top: 284px;
    left: 640px;
    width: 540px;
    display: flex;
    justify-content: center;
    align-items: center;
    gap: 30px;
  }
  .contact-item {
    display: flex;
    align-items: center;
    gap: 12px;
    color: var(--navy);
    font-weight: 800;
    white-space: nowrap;
  }
  .contact-web { font-size: 27px; }
  .contact-phone { font-size: 30px; }
  .contact-icon {
    width: 34px;
    height: 34px;
    background: var(--red);
    display: flex;
    align-items: center;
    justify-content: center;
    flex-shrink: 0;
  }
</style>
</head>
<body>
  <section class="billboard">
    <svg class="billboard-shapes" viewBox="0 0 1200 375" xmlns="http://www.w3.org/2000/svg">
      <polygon class="photo-area" role="img"
        aria-label="Photo of a backyard with a raised deck, patio seating and a putting green"
        points="0,0 705,0 575,375 0,375" fill="var(--photo-fill)"/>
      <polygon class="accent-stripe" points="700,0 752,0 622,375 570,375" fill="var(--red)"/>
      <polygon class="headline-band" points="726,112 1128,112 1168,0 1200,0 1200,242 682,242" fill="var(--navy)"/>
      <polygon class="corner-accent" points="1200,262 1200,375 1160,375" fill="var(--red)"/>
      <rect class="base-line" x="600" y="369" width="600" height="6" fill="var(--red)"/>
    </svg>

    <div class="brand-name">PLANK QR</div>

    <h1 class="headline">OUTDOOR<br>LIVING SPACES</h1>

    <div class="contact-row">
      <div class="contact-item contact-web">
        <span class="contact-icon">
          <svg width="24" height="24" viewBox="0 0 24 24" fill="none" stroke="#fff" stroke-width="1.6">
            <circle cx="12" cy="12" r="9"/>
            <ellipse cx="12" cy="12" rx="4" ry="9"/>
            <line x1="3" y1="12" x2="21" y2="12"/>
            <path d="M5 7.5h14M5 16.5h14"/>
          </svg>
        </span>
        plankqr.ca
      </div>
      <div class="contact-item contact-phone">
        <span class="contact-icon">
          <svg width="22" height="22" viewBox="0 0 24 24" fill="#fff">
            <path d="M6.6 10.8a15.1 15.1 0 0 0 6.6 6.6l2.2-2.2c.3-.3.7-.4 1-.2 1.1.4 2.3.6 3.6.6.6 0 1 .4 1 1V20c0 .6-.4 1-1 1A17 17 0 0 1 3 4c0-.6.4-1 1-1h3.5c.6 0 1 .4 1 1 0 1.3.2 2.5.6 3.6.1.3 0 .7-.2 1z"/>
          </svg>
        </span>
        416-283-9061
      </div>
    </div>
  </section>
</body>
</html>
```